Selvin: A Friday night in the Prophetic Flyer

We are holding 2 Friday night events, one on 10/25/19 and the other on 11/29/19.
The time frame is 6:30pm-9:00pm. These services will be a time of prayer/healing for the sick and will be prophetic as well. (There will be prophets prophesying over people)

The event is called: Selvin: A Friday night in the Prophetic
The flyer should also include the phrase/excerpt: "And they prophesied also".

Keywords/Phrases: Prophetic, Healing, Climbing in the Spirit, Higher level of Anointing...

Target Market(s)

those looking for healing, seeking a word from God

Colors

Designer to choose colors to be used in the design.

Requirements
Must have
• The event is called: Selvin: A Friday night in the Prophetic
• The flyer should also include the phrase/excerpt: "And they prophesied also".
• It must include the Tovik logo attached, either is fine, we have attached two different versions.
• It must have the dates, location, time
• Dates: October 25, 2019 and November 29, 2019
• Location: Hollard Community Center
• (Downtown Portland) 482 Wendle Street
• Portland, ME 04102
• Time: 6:30pm-9:00pm
• Contact Info: Tel. 207-555-3841
• email: contact@brimfield-hall.org
• web: www.tovik.org
Nice to have
• creativity in color scheme, the meaning of the word Selvin conveyed in a classy artistic way/design.
Should not have
• Crosses, pictures of churches

```html
<!DOCTYPE html>
<html lang="en">
<head>
<meta charset="utf-8">
<title>Selvin: A Friday Night in the Prophetic</title>
<link href="https://fonts.googleapis.com/css2?family=Cinzel:wght@600;700;800&family=Lato:wght@400;700;900&display=swap" rel="stylesheet">
<style>
  :root {
    --page: #f3f3f6;
    --ink: #1f1a63;
    --deep: #241b6e;
    --mist: #e4e2f0;
    --lavender: #b9b5d8;
    --white: #ffffff;
    --logo-bg: #0f2d52;
    --logo-text: #f5a524;
    --footer: #e6e5ef;
  }
  * { box-sizing: border-box; margin: 0; padding: 0; }
  html, body { width: 1200px; height: 1000px; overflow: hidden; }
  body { background: var(--page); font-family: "Lato", sans-serif; }

  .flyer {
    position: absolute; left: 261px; top: 20px;
    width: 678px; height: 960px; overflow: hidden;
    background: linear-gradient(180deg, var(--mist) 0%, #d4d1e8 30%, #8f89c0 48%, var(--deep) 63%, var(--deep) 100%);
    box-shadow: 0 18px 40px rgba(20, 16, 60, 0.25);
  }
  .crowd-photo {
    position: absolute; left: 0; top: 330px; width: 678px; height: 390px;
    background: linear-gradient(180deg, rgba(228,226,240,0) 0%, rgba(110,102,170,0.55) 30%, rgba(36,27,110,0.95) 70%, var(--deep) 100%);
  }
  .light-rays {
    position: absolute; left: 0; top: 0; width: 678px; height: 560px;
    background: radial-gradient(ellipse at 50% 80%, rgba(255,255,255,0.85) 0%, rgba(255,255,255,0) 55%);
  }
  .dove { position: absolute; width: 110px; height: 80px; border-radius: 50%;
    background: radial-gradient(ellipse, rgba(255,255,255,0.9) 0%, rgba(255,255,255,0) 70%); }
  .dove--left { left: 20px; top: 58px; }
  .dove--right { left: 508px; top: 22px; }

  .logo {
    position: absolute; left: 289px; top: 0; width: 101px; height: 116px;
    background: var(--logo-bg);
    display: flex; align-items: center; justify-content: center;
  }
  .logo__name { font-family: "Cinzel", serif; font-weight: 600; font-size: 23px; color: var(--logo-text); letter-spacing: 1px; }

  .centered { position: absolute; left: 0; width: 678px; text-align: center; }
  .title-top { top: 136px; font-family: "Cinzel", serif; font-weight: 700; font-size: 44px; color: var(--ink); line-height: 1; }
  .title-main { top: 180px; font-family: "Cinzel", serif; font-weight: 800; font-size: 152px; color: var(--ink); line-height: 1;
    letter-spacing: 2px; text-shadow: 4px 4px 0 var(--lavender); }
  .title-sub { top: 306px; font-family: "Cinzel", serif; font-weight: 700; font-size: 49px; color: var(--ink); line-height: 1; }
  .tagline { top: 352px; font-size: 12px; letter-spacing: 5px; color: var(--ink); font-weight: 700; }

  .pill {
    position: absolute; border-radius: 8px;
    background: linear-gradient(180deg, #ffffff 0%, #f0f0f4 55%, #c9c9d3 100%);
    color: var(--ink); font-weight: 900; text-align: center;
    display: flex; align-items: center; justify-content: center;
  }
  .pill--dates { left: 157px; top: 616px; width: 364px; height: 34px; font-size: 24px; }
  .pill--time { left: 169px; top: 739px; width: 340px; height: 34px; font-size: 24px; }

  .venue { top: 661px; font-size: 27px; font-weight: 900; letter-spacing: 2px; color: var(--white); }
  .dots { position: absolute; border-top: 3px dotted var(--white); }
  .dots--wide { left: 66px; top: 698px; width: 546px; }
  .dots--short { left: 171px; top: 838px; width: 336px; }
  .address { top: 706px; font-size: 20px; color: var(--white); }
  .keywords { top: 795px; font-size: 15px; line-height: 19px; color: var(--white); }
  .notes { top: 852px; font-size: 12.5px; line-height: 16px; color: var(--white); }

  .footer {
    position: absolute; left: 0; top: 909px; width: 678px; height: 51px;
    background: var(--footer); border-bottom: 1px solid var(--ink);
    display: flex; align-items: center; justify-content: center;
    font-size: 14.5px; color: var(--ink);
  }
</style>
</head>
<body>
  <main class="flyer">
    <div class="crowd-photo" role="img" aria-label="Worship crowd with raised hands under stage lights, tinted purple"></div>
    <div class="light-rays"></div>
    <div class="dove dove--left" role="img" aria-label="White dove in flight"></div>
    <div class="dove dove--right" role="img" aria-label="White dove in flight"></div>

    <div class="logo"><span class="logo__name">TOVIK</span></div>

    <h1>
      <span class="centered title-top">SELVIN A FRIDAY</span>
      <span class="centered title-main">NIGHT</span>
      <span class="centered title-sub">IN THE PROPHETIC</span>
    </h1>
    <p class="centered tagline">"AND THEY PROPHESIED ALSO"</p>

    <div class="pill pill--dates">OCT.25.19 AND NOV.29.19</div>
    <p class="centered venue">AT HOLLARD COMMUNITY CENTER</p>
    <div class="dots dots--wide"></div>
    <p class="centered address">482 WENDLE STREET, PORTLAND, ME 04102</p>
    <div class="pill pill--time">TIME: 6:30PM-9:00PM</div>

    <p class="centered keywords">PROPHETIC | HEALING<br>CLIMBING IN THE SPIRIT | HIGHER LEVEL OF ANOINTING</p>
    <div class="dots dots--short"></div>
    <p class="centered notes">THESE SERVICES WILL BE A TIME OF PRAYER/HEALING FOR THE SICK AND<br>WILL BE PROPHETIC AS WELL. (THERE WILL BE PROPHETS PROPHESYING OVER PEOPLE)</p>

    <footer class="footer">TEL. 207-555-3841 | EMAIL: CONTACT@BRIMFIELD-HALL.ORG | WWW.TOVIK.ORG</footer>
  </main>
</body>
</html>
```